Flyer
Sehr schnelle und seriöse Abwicklung. Jederzeit wieder!
Zielgruppe
Die TOLP GMBH steht Gewerbe- und Industriekunden in verschiedensten Bereichen zur Seite. Zielsetzung unserer Ingenieur- und Energiedienstleistungen ist eine niedrigere Energiekostenbelastung, eine Subventionsmaximierung für Ihre geplanten und zukünftigen Investitionen/Projekte und die nachhaltige Nutzung regenerativer Quellen zur Eigenversorgung mit Energie und Senkung des CO2-Ausstoßes!
Aufgabenstellung
Grundlegende Überschrift über den Flyer sollte sein: Energiekosten halbieren - mit unserem 4-Säulen Programm. Diese 4 Säulen sind:
Die vier zentralen Komponenten sind:
Energieaudit gemäß DIN 16247-1 : Dieses Audit, das durch das Zentralbehörde für Gewerbe gefördert wird, beinhaltet eine anschließende detaillierte Inspektion der Betriebsstätte durch einen qualifizierten Ingenieur, der die Energiebräuche analysiert und einen umfassenden Bericht erstellt. Dieser zeigt auf, wie das Unternehmen auch ohne Investitionen Energie sparen kann, wobei die aktuelle durchschnittliche Einsparung bei 21 % liegt. Unsere Ingenieure sind alle ZEGO-zertifiziert und arbeiten exklusiv für uns.
Beantragung von Fördergeldern : Falls das Unternehmen Investitionen plant, stehen derzeit über 8000 Förderprogramme zur Verfügung. Wir übernehmen die Prüfung und Beantragung dieses Programms für das Unternehmen. Die Fördersummen variieren, betragen im Durchschnitt jedoch 41 %.
Steueroptimierung der Energierechnung : Produzierende Unternehmen können nach Antragstellung eine Rückerstattung von 2,05 Cent pro kWh auf ihre Energierechnung erhalten. Außerdem lässt sich die Konzessionsabgabe von durchschnittlich 1,80 Cent auf 0,11 Cent senken. Diese beiden Faktoren machen in der Regel 30 % des reinen Energiepreises aus.
Verbesserung der Strom- und Gasrechnung : Durch eine Ausschreibung auf nationaler Ebene können durchschnittlich 23 % der aktuellen Energiekosten reduziert werden.

```html
<!DOCTYPE html>
<html lang="de">
<head>
<meta charset="utf-8">
<title>TOLP – Energiekosten halbieren</title>
<link href="https://fonts.googleapis.com/css2?family=Poppins:wght@300;400;500;600;700&display=swap" rel="stylesheet">
<style>
  :root {
    --stage: #ececec;
    --green: #6abf4b;
    --green-deep: #2e9e46;
    --ink: #141414;
    --ink-soft: #2b2b2b;
    --body: #4a4a4a;
    --rule: #cfcfcf;
    --card: #ffffff;
    --sky-light: #e6f4fb;
    --sky-mid: #8fd0f0;
    --sky-deep: #22aee6;
  }
  * { margin: 0; padding: 0; box-sizing: border-box; }
  html, body { width: 900px; height: 1200px; overflow: hidden; background: var(--stage); }
  body { font-family: "Poppins", sans-serif; position: relative; }

  .flyer {
    position: absolute; left: 26px; top: 0;
    width: 848px; height: 1200px; overflow: hidden;
    background: var(--green);
  }
  .hero-photo {
    position: absolute; left: 0; top: 0; width: 848px; height: 840px;
    background:
      linear-gradient(180deg, rgba(255,255,255,0) 55%, rgba(40,60,120,.35) 100%),
      linear-gradient(110deg, var(--sky-light) 0%, #c6e8f8 35%, var(--sky-mid) 62%, var(--sky-deep) 100%);
  }
  .hill { position: absolute; left: 0; top: 0; width: 848px; height: 1200px; }

  .brand {
    position: absolute; left: 61px; top: 78px;
    display: flex; align-items: center; gap: 12px;
    font-weight: 500; font-size: 17px; color: var(--ink-soft); letter-spacing: .5px;
  }
  .brand-square { width: 22px; height: 22px; background: var(--green); }

  .headline { position: absolute; left: 58px; top: 188px; font-weight: 700; line-height: 1; letter-spacing: -1px; }
  .headline .accent { display: block; color: var(--green); font-size: 76px; }
  .headline .main { display: block; color: var(--ink); font-size: 76px; margin-top: 6px; }
  .subline {
    position: absolute; left: 61px; top: 364px;
    font-size: 29px; line-height: 33px; font-weight: 400; color: var(--ink-soft);
  }
  .rule { position: absolute; left: 61px; top: 470px; width: 56px; height: 3px; background: var(--green); }

  .pillar {
    position: absolute; width: 355px; background: var(--card); border-radius: 20px;
  }
  .pillar-head { position: absolute; left: 28px; top: 24px; display: flex; align-items: flex-start; }
  .pillar-number {
    font-size: 31px; font-weight: 300; color: var(--green); line-height: 34px;
    width: 49px; padding-top: 2px; letter-spacing: -1px;
  }
  .pillar-divider { width: 1px; height: 34px; background: var(--rule); margin-right: 15px; margin-top: 1px; }
  .pillar-title { font-size: 17.5px; font-weight: 600; color: var(--ink); line-height: 20px; }
  .pillar-text {
    position: absolute; left: 28px; width: 302px;
    font-size: 13.2px; line-height: 17.2px; font-weight: 300; color: var(--body);
    hyphens: auto;
  }
  .p1 { left: 61px; top: 573px; height: 294px; }
  .p3 { left: 433px; top: 573px; height: 294px; }
  .p2 { left: 61px; top: 889px; height: 204px; }
  .p4 { left: 433px; top: 889px; height: 204px; }
  .p1 .pillar-text, .p2 .pillar-text { top: 78px; }
  .p3 .pillar-text { top: 108px; }
  .p4 .pillar-text { top: 96px; }

  .contact {
    position: absolute; left: 61px; right: 60px; top: 1136px;
    display: flex; align-items: center; justify-content: space-between; color: #fff;
  }
  .contact-call { font-size: 21px; font-weight: 600; }
  .contact-details { display: flex; align-items: center; gap: 18px; font-size: 17px; font-weight: 400; }
  .contact-item { display: flex; align-items: center; gap: 12px; }
  .contact-item svg { opacity: .75; }
  .base-band { position: absolute; left: 0; bottom: 0; width: 848px; height: 8px; background: var(--green-deep); }
</style>
</head>
<body>
<main class="flyer">
  <div class="hero-photo" role="img" aria-label="Foto: Industrieanlage, Windrad, Bäume und Solarmodule unter blauem Himmel"></div>
  <svg class="hill" viewBox="0 0 848 1200" aria-hidden="true">
    <path d="M0,690 C200,665 520,680 848,810 L848,1200 L0,1200 Z" fill="#2e9e46"/>
    <path d="M0,676 C260,640 600,700 848,840 L848,1200 L0,1200 Z" fill="#7cc44c"/>
    <path d="M0,760 C300,740 620,800 848,900 L848,1200 L0,1200 Z" fill="#6abf4b"/>
  </svg>

  <div class="brand"><span class="brand-square"></span><span>TOLP Tollberger Institut für Klimaschutz</span></div>

  <h1 class="headline"><span class="accent">Energiekosten</span><span class="main">halbieren</span></h1>
  <p class="subline">mit unserem 4-Säulen<br>Programm.</p>
  <div class="rule"></div>

  <section class="pillar p1">
    <div class="pillar-head"><span class="pillar-number">01</span><span class="pillar-divider"></span><h2 class="pillar-title">Energieaudit gemäß<br>DIN 16247</h2></div>
    <p class="pillar-text">Dieses Audit, das durch die Zentralbehörde für Gewerbe gefördert wird, beinhaltet eine anschließende detaillierte Inspektion der Betriebsstätte durch einen qualifizierten Ingenieur, der die Energiebräuche analysiert und einen umfassenden Bericht erstellt. Dieser zeigt auf, wie das Unternehmen auch ohne Investitionen Energie sparen kann, wobei die aktuelle durchschnittliche Einsparung bei 21 % liegt. Unsere Ingenieure sind alle ZEGO-zertifiziert und arbeiten exklusiv für uns.</p>
  </section>

  <section class="pillar p3">
    <div class="pillar-head"><span class="pillar-number">03</span><span class="pillar-divider"></span><h2 class="pillar-title">Steueroptimierung<br>der Energierechnung</h2></div>
    <p class="pillar-text">Produzierende Unternehmen können nach Antragstellung eine Rückerstattung von 2,05 Cent pro kWh auf ihre Energierechnung erhalten. Außerdem lässt sich die Konzessionsabgabe von durchschnittlich 1,80 Cent auf 0,11 Cent senken. Diese beiden Faktoren machen in der Regel 30 % des reinen Energiepreises aus.</p>
  </section>

  <section class="pillar p2">
    <div class="pillar-head"><span class="pillar-number">02</span><span class="pillar-divider"></span><h2 class="pillar-title">Beantragung<br>von Fördergeldern</h2></div>
    <p class="pillar-text">Falls das Unternehmen Investitionen plant, stehen derzeit über 8000 Förderprogramme zur Verfügung. Wir übernehmen die Prüfung und Beantragung dieses Programms für das Unternehmen. Die Fördersummen variieren, betragen im Durchschnitt jedoch 41 %.</p>
  </section>

  <section class="pillar p4">
    <div class="pillar-head"><span class="pillar-number">04</span><span class="pillar-divider"></span><h2 class="pillar-title">Verbesserung der Strom-<br>und Gasrechnung</h2></div>
    <p class="pillar-text">Durch eine Ausschreibung auf nationaler Ebene können durchschnittlich 23 % der aktuellen Energiekosten reduziert werden.</p>
  </section>

  <footer class="contact">
    <span class="contact-call">Kontaktieren Sie uns</span>
    <div class="contact-details">
      <span class="contact-item">
        <svg width="16" height="16" viewBox="0 0 16 16" aria-hidden="true"><rect x="0.5" y="3" width="4" height="12" rx="1" fill="#fff"/><rect x="5.5" y="1" width="10" height="14" rx="1" fill="none" stroke="#fff" stroke-width="1.4"/><rect x="8" y="4" width="5" height="3" fill="#fff"/><g fill="#fff"><rect x="8" y="9" width="1.5" height="1.5"/><rect x="11" y="9" width="1.5" height="1.5"/><rect x="8" y="12" width="1.5" height="1.5"/><rect x="11" y="12" width="1.5" height="1.5"/></g></svg>
        0123 4567890
      </span>
      <span class="contact-item">
        <svg width="16" height="12" viewBox="0 0 16 12" aria-hidden="true"><rect width="16" height="12" rx="1.5" fill="#fff"/><path d="M1 1.5 L8 7 L15 1.5" fill="none" stroke="#6abf4b" stroke-width="1.4"/></svg>
        info@tolp-beispiel.de
      </span>
    </div>
  </footer>
  <div class="base-band"></div>
</main>
</body>
</html>
```